Business card with logo for a family psychologist

I need a business card for my private practice in the urban Chicago area as a psychologist. I see families and individuals who are going through difficult times - divorce, separation, illness, or trauma. I want to project hopefulness, competence, and caring.

Target Market(s)

Adults, other professionals - such as physicans and lawyers

Industry/Entity Type

Health Care

Contact Information for Business Card

Front should have my name and credentials; back should have location information including my email, phone

Font styles to use
Serif
Decorative
Script

Requirements
Must have
• Unique logo
Should not have
• No pictures or icons of people; no black

```html
<!DOCTYPE html>
<html lang="en">
<head>
<meta charset="utf-8">
<title>Dr. Laurel Hayes – Business Card</title>
<link rel="stylesheet" href="https://fonts.googleapis.com/css2?family=Cormorant+Garamond:wght@600&family=Cinzel:wght@400&family=Arimo:wght@400&display=swap">
<style>
  :root {
    --purple: #7d5cc0;
    --purple-deep: #6a4bb0;
    --gold: #f1b95a;
    --tagline: #f0b457;
    --card: #fbfbfb;
    --ink: #2c2c34;
    --backdrop: #ece8e2;
  }
  * { box-sizing: border-box; margin: 0; padding: 0; }
  html, body { width: 1200px; height: 902px; overflow: hidden; }
  body { background: var(--backdrop); position: relative; }

  .card {
    position: absolute;
    width: 640px;
    height: 366px;
    background: var(--card);
    border-radius: 4px;
    box-shadow: 0 10px 28px rgba(60, 50, 40, 0.18);
    overflow: hidden;
  }
  .card--front { left: 80px; top: 64px; }
  .card--back { left: 480px; top: 472px; }

  .wordmark {
    font-family: "Cormorant Garamond", serif;
    font-weight: 600;
    color: var(--purple);
    white-space: nowrap;
    line-height: 1;
  }
  .tagline {
    font-family: "Cinzel", serif;
    color: var(--tagline);
    letter-spacing: 0.02em;
    white-space: nowrap;
    line-height: 1;
  }

  .card--front .identity {
    position: absolute;
    left: 0; right: 0; top: 128px;
    text-align: center;
  }
  .card--front .wordmark { font-size: 62px; }
  .card--front .tagline { font-size: 25px; margin-top: 8px; }

  .card__swoosh { position: absolute; inset: 0; width: 640px; height: 366px; }

  .card--back .identity { position: absolute; left: 40px; top: 56px; }
  .card--back .wordmark { font-size: 46px; }
  .card--back .tagline { font-size: 18px; margin-top: 6px; }

  .contact {
    position: absolute;
    left: 118px;
    top: 210px;
    list-style: none;
    font-family: "Arimo", sans-serif;
    font-size: 17px;
    color: var(--ink);
  }
  .contact__item { display: flex; align-items: flex-start; gap: 10px; margin-bottom: 9px; line-height: 1.25; }
  .contact__icon { width: 20px; height: 20px; flex: none; margin-top: 1px; }
</style>
</head>
<body>

  <section class="card card--front" aria-label="Card front">
    <div class="identity">
      <div class="wordmark">Dr. Laurel Hayes Ph.D.</div>
      <div class="tagline">Licensed Clinical Psychologist</div>
    </div>
  </section>

  <section class="card card--back" aria-label="Card back">
    <svg class="card__swoosh" viewBox="0 0 640 366" aria-hidden="true">
      <defs>
        <linearGradient id="purpleFill" x1="0" y1="0" x2="1" y2="1">
          <stop offset="0" stop-color="#8a6bd0"/>
          <stop offset="1" stop-color="#6646ad"/>
        </linearGradient>
      </defs>
      <path d="M420 0 C520 110 470 290 240 366 L640 366 L640 0 Z" fill="var(--gold)"/>
      <path d="M488 0 C560 130 500 300 300 366 L640 366 L640 0 Z" fill="url(#purpleFill)" stroke="#ffffff" stroke-width="3"/>
    </svg>

    <div class="identity">
      <div class="wordmark">Dr. Laurel Hayes Ph.D.</div>
      <div class="tagline">Licensed Clinical Psychologist</div>
    </div>

    <ul class="contact">
      <li class="contact__item">
        <svg class="contact__icon" viewBox="0 0 20 20" aria-hidden="true">
          <rect width="20" height="20" rx="2" fill="var(--purple)"/>
          <path d="M6 4.5 L8.3 4.5 L9.2 7.5 L7.8 8.6 C8.5 10.2 9.8 11.5 11.4 12.2 L12.5 10.8 L15.5 11.7 L15.5 14 C15.5 14.8 14.8 15.5 14 15.5 C9.2 15.2 4.8 10.8 4.5 6 C4.5 5.2 5.2 4.5 6 4.5 Z" fill="#fff"/>
        </svg>
        <span>312-555-0148</span>
      </li>
      <li class="contact__item">
        <svg class="contact__icon" viewBox="0 0 20 20" aria-hidden="true">
          <rect width="20" height="20" rx="2" fill="var(--purple)"/>
          <rect x="4" y="6" width="12" height="8.5" fill="none" stroke="#fff" stroke-width="1.4"/>
          <path d="M4 6 L10 11 L16 6" fill="none" stroke="#fff" stroke-width="1.4"/>
        </svg>
        <span>drlaurelhayes@mailbox.com</span>
      </li>
      <li class="contact__item">
        <svg class="contact__icon" viewBox="0 0 20 20" aria-hidden="true">
          <rect width="20" height="20" rx="2" fill="var(--purple)"/>
          <path d="M10 3.8 C7.3 3.8 5.5 5.8 5.5 8.2 C5.5 11.2 10 16.2 10 16.2 C10 16.2 14.5 11.2 14.5 8.2 C14.5 5.8 12.7 3.8 10 3.8 Z" fill="#fff"/>
          <circle cx="10" cy="8.2" r="1.7" fill="var(--purple)"/>
        </svg>
        <span>240 W. Lakeview Suite 810<br>Chicago, Illinois 60610</span>
      </li>
    </ul>
  </section>

</body>
</html>
```